PowerPoint Design Project

Hi,

Using our logo, we would like a designer to provide us with a powerpoint template that has a unique brand.

To us this means creating a color palette, treatment, a font that plays off of our logo. The color palette needs to blend well with our existing colors, but give us some options, make things "POP".

The color palette needs to include the colors (with RGB numbers), gradients, different graphic styles (solid, transparent, gradient, image fills) and lines (a callout leader line, a multi-color bar to divide content)

The palette and treatment must extend itself to graphs, charts and images.

We would also like to see different parts of our logo applied to the different template slides. For example, on a title slide we would like the image with our logo and tagline. With the end slide we would like to see our logo and URL. We also attached our logo without the tagline and also just the colored cube. So please be creative on how these are incorporated into the deck.

Images are attached.

Thank you
Calvin

Reason: We are extending the deadline 1 day.

Large Corporations

• color palette, treatments and consistent fonts. color palette must complement our logo. color palette must extend to graphs, charts and images.

different logo's incorprated into the deck. For example, on a title slide we would like the image with our logo and tagline. With the end slide we would like to see our logo and URL. We also attached our logo without the tagline and also just the colored cube. So please be creative on how these are incorporated into the deck.
• We do not want to see designers taking the logo and incorporating them into the background and calling it a template.

```html
<!DOCTYPE html>
<html lang="en">
<head>
<meta charset="utf-8">
<title>Tarnvale presentation template</title>
<link rel="stylesheet" href="https://fonts.googleapis.com/css2?family=Cabin:wght@400;500;600;700&display=swap">
<style>
  :root{
    --stage:#b4b6bd;
    --green:#6cc04a;
    --green-bright:#80d23d;
    --green-deep:#169a4a;
    --blue:#3aa3d4;
    --blue-deep:#2d6fb8;
    --slate:#3f4250;
    --slate-deep:#2b2d38;
    --ink:#2a2a2a;
    --muted:#c3c6ce;
    --paper:#f4f5f8;
    --rule:#cfd2da;
  }
  *{margin:0;padding:0;box-sizing:border-box}
  html,body{width:1200px;height:919px;overflow:hidden}
  body{background:var(--stage);font-family:"Cabin",sans-serif;position:relative;color:var(--ink)}
  .slide{position:absolute;width:582px;height:436px;overflow:hidden;background:linear-gradient(180deg,#fff 0%,var(--paper) 100%)}
  .slide--title{left:14px;top:16px;background:linear-gradient(180deg,#80c242 0%,#3daf48 55%,#139a4c 100%)}
  .slide--chart{left:605px;top:16px}
  .slide--content{left:14px;top:467px}
  .slide--end{left:605px;top:467px}

  .title-lockup{position:absolute;left:94px;top:180px;display:flex;align-items:center;gap:18px}
  .title-lockup__mark{width:44px;height:44px;background:var(--green-bright)}
  .title-lockup__word{font-size:62px;font-weight:600;color:var(--green-bright);letter-spacing:1px;line-height:1}

  .slide__topbar{position:absolute;left:0;top:0;width:100%;height:4px;background:var(--green)}
  .slide__heading{position:absolute;left:7px;top:12px;font-size:20px;font-weight:600;color:var(--green)}
  .slide__rule{position:absolute;left:0;top:38px;width:280px;height:1px;background:var(--rule)}
  .slide__brand{position:absolute;left:292px;top:26px;font-size:20px;font-weight:600;color:var(--muted)}
  .slide__footer{position:absolute;left:0;bottom:0;width:100%;height:44px;background:linear-gradient(180deg,#4a4d5b 0%,var(--slate-deep) 100%)}
  .slide__page{position:absolute;left:14px;top:17px;font-size:9px;color:var(--green)}
  .slide__contact{position:absolute;top:16px;font-size:9px;color:var(--green)}
  .slide__contact--mail{right:326px}
  .slide__contact--web{left:311px}
  .slide__footer-mark{position:absolute;left:278px;top:13px;width:16px;height:16px;background:var(--blue)}

  .chart{position:absolute;left:0;top:0;width:582px;height:392px}
  .chart text{font-family:"Cabin",sans-serif;font-size:9px;fill:#222}

  .portrait{position:absolute;left:30px;top:48px;width:201px;height:343px;background:linear-gradient(180deg,#eef0f3 0%,#2a3140 35%,#1c2330 100%);border-radius:40px 40px 0 0}
  .points{position:absolute;left:261px;top:80px;width:300px}
  .points__group + .points__group{margin-top:22px;padding-top:16px;border-top:1px solid #dde0e6}
  .points__title{font-size:12px;color:var(--green);margin:0 0 1px 20px}
  .points__item{position:relative;padding-left:20px;font-size:8.6px;line-height:12.3px;color:#333;margin-bottom:12px}
  .points__item::before{content:"";position:absolute;left:0;top:0;width:10px;height:10px;background:linear-gradient(135deg,var(--blue) 50%,var(--green) 50%)}

  .end-lockup{position:absolute;left:93px;top:170px;display:flex;align-items:center;gap:16px}
  .end-lockup__mark{width:72px;height:72px;background:var(--green)}
  .end-lockup__word{font-size:50px;font-weight:700;color:var(--slate-deep);line-height:1}
  .end-lockup__url{font-size:14px;color:var(--blue-deep);margin-top:4px}
</style>
</head>
<body>

<section class="slide slide--title">
  <div class="title-lockup">
    <div class="title-lockup__mark"></div>
    <div class="title-lockup__word">elevate</div>
  </div>
</section>

<section class="slide slide--chart">
  <div class="slide__topbar"></div>
  <h2 class="slide__heading">charts</h2>
  <div class="slide__rule"></div>
  <div class="slide__brand">tarnvale</div>
  <svg class="chart" viewBox="0 0 582 392" aria-label="Bar chart of goals, results and revenue per trimester">
    <defs>
      <linearGradient id="barGreen" x1="0" y1="0" x2="0" y2="1"><stop offset="0" stop-color="#7cc545"/><stop offset="1" stop-color="#3ea64a"/></linearGradient>
      <linearGradient id="barBlue" x1="0" y1="0" x2="0" y2="1"><stop offset="0" stop-color="#3aa7d6"/><stop offset="1" stop-color="#2f76bb"/></linearGradient>
      <linearGradient id="barSlate" x1="0" y1="0" x2="0" y2="1"><stop offset="0" stop-color="#474a58"/><stop offset="1" stop-color="#2c2e39"/></linearGradient>
    </defs>
    <rect x="54" y="92" width="441" height="256" fill="#fff"/>
    <g stroke="#d9dbe1" stroke-width="1">
      <line x1="54" y1="92" x2="495" y2="92"/><line x1="54" y1="134.7" x2="495" y2="134.7"/>
      <line x1="54" y1="177.3" x2="495" y2="177.3"/><line x1="54" y1="220" x2="495" y2="220"/>
      <line x1="54" y1="262.7" x2="495" y2="262.7"/><line x1="54" y1="305.3" x2="495" y2="305.3"/>
      <line x1="54" y1="92" x2="54" y2="348"/><line x1="495" y1="92" x2="495" y2="348"/>
    </g>
    <line x1="54" y1="348" x2="495" y2="348" stroke="#b8bbc4"/>
    <g text-anchor="end">
      <text x="45" y="95">6</text><text x="45" y="138">5</text><text x="45" y="180">4</text>
      <text x="45" y="223">3</text><text x="45" y="266">2</text><text x="45" y="308">1</text><text x="45" y="351">0</text>
    </g>
    <rect x="73" y="164.5" width="25" height="183.5" fill="url(#barGreen)"/>
    <rect x="98" y="245.6" width="25" height="102.4" fill="url(#barBlue)"/>
    <rect x="123" y="262.7" width="25" height="85.3" fill="url(#barSlate)"/>
    <rect x="183.25" y="241.3" width="25" height="106.7" fill="url(#barGreen)"/>
    <rect x="208.25" y="160.3" width="25" height="187.7" fill="url(#barBlue)"/>
    <rect x="233.25" y="262.7" width="25" height="85.3" fill="url(#barSlate)"/>
    <rect x="293.5" y="198.7" width="25" height="149.3" fill="url(#barGreen)"/>
    <rect x="318.5" y="271.2" width="25" height="76.8" fill="url(#barBlue)"/>
    <rect x="343.5" y="220" width="25" height="128" fill="url(#barSlate)"/>
    <rect x="403.75" y="156" width="25" height="192" fill="url(#barGreen)"/>
    <rect x="428.75" y="228.5" width="25" height="119.5" fill="url(#barBlue)"/>
    <rect x="453.75" y="134.7" width="25" height="213.3" fill="url(#barSlate)"/>
    <g text-anchor="middle">
      <text x="110.5" y="364">1 Trimester</text><text x="220.75" y="364">2 Trimester</text>
      <text x="331" y="364">3 Trimester</text><text x="441.25" y="364">4 Trimester</text>
    </g>
    <rect x="512" y="93" width="7" height="7" fill="#6cbf48"/><text x="523" y="100">Goals</text>
    <rect x="512" y="110" width="7" height="7" fill="#38a0d2"/><text x="523" y="117">Results</text>
    <rect x="512" y="126" width="7" height="7" fill="#3a3d4a"/><text x="523" y="133">Revenue</text>
  </svg>
  <footer class="slide__footer">
    <span class="slide__page">6</span>
    <span class="slide__contact slide__contact--mail">info@tarnvale.com</span>
    <span class="slide__footer-mark"></span>
    <span class="slide__contact slide__contact--web">www.tarnvale.com</span>
  </footer>
</section>

<section class="slide slide--content">
  <div class="slide__topbar"></div>
  <h2 class="slide__heading">elevate</h2>
  <div class="slide__rule"></div>
  <div class="slide__brand">tarnvale</div>
  <div class="portrait" role="img" aria-label="Portrait photo of a young businessman in a dark suit with a green shirt and tie"></div>
  <div class="points">
    <div class="points__group">
      <h3 class="points__title">Analyze</h3>
      <p class="points__item">Aenean ridiculus tortor quis interdum id habitant ad, natoque consectetuer nisl auctor libero quisque euismod ante inceptos malesuada ligula mattis.</p>
      <p class="points__item">Nulla, netus pulvinar pellentesque porttitor purus maecenas tellus hac nulla lacus. Lorem. Nostra laoreet nulla, dis cursus nascetur dolor odio Eu Magna molestie montes dui mus cursus habitasse mauris tempor.</p>
      <p class="points__item">Varius inceptos nascetur mollis dui aptent ultrices. Pretium pulvinar ante lobortis convallis lectus netus vitae penatibus eros at blandit. Parturient.</p>
    </div>
    <div class="points__group">
      <h3 class="points__title">Elevate</h3>
      <p class="points__item">Aenean ridiculus tortor quis interdum id habitant ad, natoque consectetuer nisl auctor libero quisque euismod ante inceptos malesuada ligula mattis.</p>
      <p class="points__item">Nulla, netus pulvinar pellentesque porttitor purus maecenas tellus hac nulla lacus. Lorem. Nostra laoreet nulla, dis cursus nascetur dolor odio</p>
    </div>
  </div>
  <footer class="slide__footer">
    <span class="slide__page">7</span>
    <span class="slide__contact slide__contact--mail">info@tarnvale.com</span>
    <span class="slide__footer-mark"></span>
    <span class="slide__contact slide__contact--web">www.tarnvale.com</span>
  </footer>
</section>

<section class="slide slide--end">
  <div class="end-lockup">
    <div class="end-lockup__mark"></div>
    <div>
      <div class="end-lockup__word">tarnvale</div>
      <div class="end-lockup__url">www.tarnvale.com</div>
    </div>
  </div>
</section>

</body>
</html>
```